Startup Technology Consulting Firm in NYC Needs A Website

I need a website built for my startup technology consulting company Brightmoor Systems Collective. We offer a unique white glove service that provides end to end technology support. I want to stand out above the rest. We are small firm but are very dedicated which where we derive our name from BSC primarily offers
end to end technology advisory services to small businesses lacking their own IT staff. We offer top notch white glove and our customer service and satisfaction is exceed by no one.

Below are some of what we provide our clients

Strategic IT Planning
Business Continuity Planning/Disaster Recovery
Cloud Computing\DataCenter Solutions
Server Infrastructure/Networking
Virtualization Technologies
Project Management

Our Technology Advisors hold many certifications from Quillora & Tessfold. We are also Quillora Partners

I have attached my logo (preview design) As soon as I ge the final images I will upload.

Reason: want to give more time to submit designs

Industry/Entity Type

Information Technology

Coding

Coded - Design and coding required

Number of Pages Required

1 page

Font styles to use
Sans Serif

Requirements
Must have
• Attract Target Market. The site should bleed the company vision
• DEDICATION everything about the site should show this
• Layout the Benefits of our offerings
• Links to my social media
• Links to dircct my client's for remote support

```html
<!DOCTYPE html>
<html lang="en">
<head>
<meta charset="utf-8">
<title>Brightmoor Systems Collective</title>
<link href="https://fonts.googleapis.com/css2?family=Open+Sans:wght@400;600;700;800&display=swap" rel="stylesheet">
<style>
:root{
  --blue:#1684d0;
  --blue-dark:#0f66a8;
  --ink:#2d2f33;
  --text:#555b62;
  --muted:#8a9098;
  --line:#e3e6ea;
  --grey-bg:#eef0f2;
  --footer:#3b3f45;
  --white:#ffffff;
}
*{box-sizing:border-box;margin:0;padding:0}
html,body{width:711px;height:1200px;overflow:hidden;background:var(--white)}
body{font-family:"Open Sans",Arial,sans-serif;color:var(--text);font-size:7px;line-height:1.45}
.topbar{height:12px;background:var(--ink);display:flex;justify-content:flex-end;align-items:center;padding-right:22px;gap:4px;color:#cfd3d8;font-size:6px}
.topbar .dot{width:8px;height:8px;border-radius:50%;background:var(--blue)}
.header{height:54px;display:flex;align-items:center;justify-content:space-between;padding:0 22px;border-bottom:1px solid var(--line)}
.brand{display:flex;align-items:center;gap:6px}
.brand .mark{width:16px;height:16px;border-radius:50%;background:var(--blue)}
.brand .name{font-weight:800;font-size:11px;color:var(--blue);line-height:1.05;text-transform:uppercase;letter-spacing:.3px}
.nav{display:flex;gap:12px;font-size:7.5px;color:var(--ink)}
.nav a{text-decoration:none;color:inherit;padding-bottom:2px}
.nav a.active{color:var(--blue);border-bottom:2px solid var(--blue);font-weight:700}
.call{display:flex;align-items:center;gap:5px}
.call svg{width:14px;height:14px}
.call small{display:block;font-size:6px;color:var(--muted)}
.call strong{font-size:11px;color:var(--blue);font-weight:700}
.hero{position:relative;height:249px}
.hero .photo{position:absolute;inset:0;background:linear-gradient(100deg,#cfd6dc 0%,#e9ecee 35%,#b9c2ca 70%,#8c969f 100%)}
.hero .caption{position:absolute;left:0;right:0;bottom:0;height:20px;background:rgba(20,22,26,.82);color:var(--white);font-weight:700;font-size:9.5px;display:flex;align-items:center;justify-content:center}
.hero .arrow{position:absolute;top:112px;width:12px;height:20px;background:rgba(0,0,0,.55)}
.hero .arrow.left{left:0}.hero .arrow.right{right:0}
.services{height:206px;background:var(--blue);color:var(--white);text-align:center;padding-top:12px}
.services h2{font-size:13px;font-weight:700}
.services .intro{font-size:6.5px;opacity:.85;margin-top:2px}
.service-row{display:flex;justify-content:space-between;padding:0 26px;margin-top:14px}
.service{width:98px}
.service .icon{width:44px;height:44px;border-radius:50%;border:3px solid var(--white);background:var(--blue-dark);margin:0 auto 8px;display:flex;align-items:center;justify-content:center}
.service .icon svg{width:20px;height:20px}
.service h3{font-size:7.5px;font-weight:700;margin-bottom:3px}
.service p{font-size:6px;opacity:.85}
.welcome{height:131px;text-align:center;padding:18px 40px 0}
.welcome h2{font-size:13px;color:var(--ink);font-weight:700}
.rule{width:40px;height:2px;background:var(--blue);margin:5px auto 8px}
.welcome p{font-size:6.5px}
.welcome a{display:block;color:var(--blue);font-size:6.5px;margin-top:4px;text-decoration:none}
.why{height:182px;background:var(--grey-bg);margin-top:18px;display:flex;padding:14px 22px 0;justify-content:space-between}
.why h2{font-size:12px;color:var(--ink);font-weight:700}
.why .rule{margin:5px 0 8px}
.why .lead{font-size:6.5px;max-width:330px;margin-bottom:6px}
.why ul{list-style:none}
.why li{display:flex;align-items:center;gap:5px;font-size:6.5px;margin-bottom:5px}
.why li::before{content:"";width:5px;height:5px;border-radius:50%;background:var(--blue)}
.video{width:235px;text-align:center}
.video .screen{height:140px;border-radius:8px;background:radial-gradient(circle at 50% 45%,#4a6f8c 0%,#1e2a36 70%)}
.video span{display:block;font-size:6.5px;color:var(--ink);margin-top:4px}
.lower{height:120px;display:flex;padding:12px 22px 0;gap:22px}
.certs{flex:1}
.lower h3{font-size:8.5px;color:var(--ink);font-weight:700;border-bottom:1px solid var(--line);padding-bottom:4px;margin-bottom:10px}
.badge-row{display:flex;gap:14px}
.badge{width:60px;text-align:center}
.badge .plate{height:34px;background:#dfe2e6;border-radius:2px}
.badge span{display:block;font-size:5.5px;margin-top:3px}
.remote{width:180px}
.remote p{font-size:6.5px;margin-bottom:6px}
.remote .field{height:14px;border:1px solid var(--line);margin-bottom:5px}
.remote .btn{display:inline-block;background:var(--blue);color:var(--white);font-size:6.5px;padding:3px 8px}
.footer{height:201px;background:var(--footer);color:#c9cdd2;display:flex;justify-content:space-between;padding:14px 22px 0;position:relative}
.contact h3{color:var(--white);font-size:8.5px;margin-bottom:8px;display:flex;gap:5px;align-items:center}
.contact h3 i{width:9px;height:9px;border-radius:50%;background:var(--blue);display:block}
.contact-item{display:flex;gap:6px;margin-bottom:8px;font-size:6.5px}
.contact-item i{width:9px;height:9px;border-radius:50%;background:#5c6168;flex:none;margin-top:1px}
.contact-item b{display:block;color:var(--white);font-weight:600}
.footer-brand{position:absolute;left:250px;top:88px;font-weight:800;font-size:15px;color:#5a5f66;text-transform:uppercase;text-align:center;line-height:1.1}
.inquiry{width:120px;background:#5a5f66;padding:8px;align-self:flex-start;margin-top:6px}
.inquiry h3{color:var(--white);font-size:9px;margin-bottom:4px}
.inquiry p{font-size:6px;margin-bottom:5px}
.inquiry .field{height:12px;background:#6d7279;font-size:5.5px;padding:2px 4px;margin-bottom:4px;color:#d5d8dc}
.inquiry .field.tall{height:24px}
.inquiry .btn{background:var(--blue);color:var(--white);font-size:6.5px;font-weight:700;padding:3px 8px;display:inline-block}
.bottombar{height:27px;background:var(--blue);color:var(--white);font-size:6px;display:flex;align-items:center;justify-content:center}
</style>
</head>
<body>
<div class="topbar">Follow Us By <span class="dot"></span><span class="dot"></span><span class="dot"></span></div>

<header class="header">
  <div class="brand"><span class="mark"></span><span class="name">Brightmoor<br>Systems Collective</span></div>
  <nav class="nav"><a class="active" href="#">Home</a><a href="#">About Us</a><a href="#">Services</a><a href="#">Why Choose Us</a><a href="#">Contact Us</a></nav>
  <div class="call">
    <svg viewBox="0 0 20 20"><path d="M5 2l3 4-2 2c1 2 3 4 5 5l2-2 4 3-2 3C9 17 3 11 2 5z" fill="#1684d0"/></svg>
    <div><small>Call Us Today</small><strong>555-014-2277</strong></div>
  </div>
</header>

<section class="hero">
  <div class="photo" role="img" aria-label="Photo of a person using a tablet at a desk"></div>
  <span class="arrow left"></span><span class="arrow right"></span>
  <div class="caption">We Offer End To End Technology Advisory Services To Small Businesses Lacking Their Own IT Staff</div>
</section>

<section class="services">
  <h2>Services We Provide</h2>
  <p class="intro">Practical guidance for growing teams, delivered with care and full attention from first call.</p>
  <div class="service-row">
    <div class="service"><div class="icon"><svg viewBox="0 0 20 20"><circle cx="10" cy="10" r="7" fill="none" stroke="#fff" stroke-width="2"/><circle cx="10" cy="10" r="2" fill="#fff"/></svg></div><h3>Strategic IT Planning</h3><p>Clear plans and steady support shaped around your business goals.</p></div>
    <div class="service"><div class="icon"><svg viewBox="0 0 20 20"><path d="M3 10a7 7 0 0 1 12-5M17 10a7 7 0 0 1-12 5" fill="none" stroke="#fff" stroke-width="2"/></svg></div><h3>Business Continuity</h3><p>Backups and recovery steps that keep your daily work running.</p></div>
    <div class="service"><div class="icon"><svg viewBox="0 0 20 20"><path d="M5 15h10a3 3 0 0 0 0-6 4 4 0 0 0-8-1 3.5 3.5 0 0 0-2 7z" fill="#fff"/></svg></div><h3>Cloud Computing</h3><p>Secure cloud and data center options sized for your team.</p></div>
    <div class="service"><div class="icon"><svg viewBox="0 0 20 20"><rect x="4" y="3" width="12" height="4" fill="#fff"/><rect x="4" y="8" width="12" height="4" fill="#fff"/><rect x="4" y="13" width="12" height="4" fill="#fff"/></svg></div><h3>Server Infrastructure</h3><p>Reliable servers and networks built to handle growth with ease.</p></div>
    <div class="service"><div class="icon"><svg viewBox="0 0 20 20"><rect x="3" y="5" width="9" height="7" fill="none" stroke="#fff" stroke-width="2"/><rect x="8" y="9" width="9" height="7" fill="#fff"/></svg></div><h3>Virtualization Technologies</h3><p>Fewer machines, more flexibility, and lower costs across every office.</p></div>
    <div class="service"><div class="icon"><svg viewBox="0 0 20 20"><path d="M4 10l4 4 8-9" fill="none" stroke="#fff" stroke-width="2.5"/></svg></div><h3>Project Management</h3><p>Every rollout tracked closely from first plan to final handoff.</p></div>
  </div>
</section>

<section class="welcome">
  <h2>Welcome to Brightmoor Systems Collective</h2>
  <div class="rule"></div>
  <p>We partner with small businesses that have no in-house IT staff, handling planning, support and upgrades so owners can focus on running their company. Every client gets a dedicated advisor who knows their systems, answers quickly and follows each request through to the finish. Our work is measured by uptime, clarity and trust.</p>
  <a href="#">Read more</a>
</section>

<section class="why">
  <div>
    <h2>Why Choose Us</h2>
    <div class="rule"></div>
    <p class="lead">Small firms deserve the same careful IT attention large companies enjoy, without the overhead.</p>
    <ul>
      <li>A single advisor who knows your systems</li>
      <li>Fast answers from people, not ticket queues</li>
      <li>Plans built around your budget and growth</li>
      <li>Proactive monitoring before problems reach you</li>
      <li>Clear reporting with no technical jargon</li>
      <li>Certified specialists across cloud and servers</li>
    </ul>
  </div>
  <div class="video">
    <div class="screen" role="img" aria-label="Video still of a tablet showing a technology presentation"></div>
    <span>View Video</span>
  </div>
</section>

<section class="lower">
  <div class="certs">
    <h3>Certifications Our Technology Advisors Hold</h3>
    <div class="badge-row">
      <div class="badge"><div class="plate"></div><span>Solutions Partner</span></div>
      <div class="badge"><div class="plate"></div><span>Systems Engineer</span></div>
      <div class="badge"><div class="plate"></div><span>Certified Professional</span></div>
      <div class="badge"><div class="plate"></div><span>Desktop Specialist</span></div>
      <div class="badge"><div class="plate"></div><span>Cloud Associate</span></div>
    </div>
  </div>
  <div class="remote">
    <h3>Remote Support</h3>
    <p>Connect with an advisor in minutes using our secure remote session tool.</p>
    <div class="field"></div>
    <span class="btn">Connect Now</span>
  </div>
</section>

<footer class="footer">
  <div class="contact">
    <h3><i></i>Contact Information</h3>
    <div class="contact-item"><i></i><div><b>Postal Address</b>48 Harlow Street, New York</div></div>
    <div class="contact-item"><i></i><div><b>Telephone</b>555-014-2277</div></div>
    <div class="contact-item"><i></i><div><b>Email</b>hello@brightmoorsc.example</div></div>
    <div class="contact-item"><i></i><div><b>Website</b>www.brightmoorsc.example</div></div>
    <div class="contact-item"><i></i><div><b>Social</b>social.example/brightmoorsc</div></div>
  </div>
  <div class="footer-brand">Brightmoor<br>Systems Collective</div>
  <div class="inquiry">
    <h3>Quick Inquiry</h3>
    <p>Send us a short note and we reply within one day.</p>
    <div class="field">Name</div>
    <div class="field">Email</div>
    <div class="field">Phone</div>
    <div class="field tall">Message</div>
    <span class="btn">SUBMIT</span>
  </div>
</footer>
<div class="bottombar">© 2024 Brightmoor Systems Collective. All rights reserved.</div>
</body>
</html>
```